Tidewell Cryotherapy brochure

I need brochure design for my Cryotherapy business.
Target market: Athletes from high School to pro, Fitness, adults needing relief from arthritic and surgical pain. Color pallet should have be in keeping with the logo blues, white and silver (attached). There should be a sections to address what full body cryo is .. and its benefits, FAQ's. a section that i can list services, prices, hours...ect.. There should also be high quality pics in keeping with the theme of rejuvenation and replenishment. Tri Fold double sided.

Target Market(s)

Target market: Athletes from high School to pro, Fitness, adults needing relief from arthritic and surgical pain.

Industry/Entity Type

Business

Colors
33a6d7
cee9f5
0255a3
cfdeed
ffffff
ecf7fb
d7d7d7
9d9d9d

Requirements
Must have
• There should be a sections to address what full body cryo is .. and its benefits, FAQ's. a section that i can list services, prices, hours...ect.. There should also be high quality pics in keeping with the theme of rejuvenation and replenishment. Tri Fold double sided.
Nice to have
• Graphics of the circulatrory system and cryo's effect on it.

```html
<!DOCTYPE html>
<html lang="en">
<head>
<meta charset="utf-8">
<title>Tidewell Cryotherapy — Brochure Spread</title>
<link rel="stylesheet" href="https://fonts.googleapis.com/css2?family=Roboto+Condensed:wght@700;900&family=Source+Sans+3:wght@400;600;700&display=swap">
<style>
:root{
  --ice-blue:#33a6d7;
  --bright-blue:#1fb4e6;
  --deep-blue:#0255a3;
  --ink:#16191c;
  --panel-dark:#1d2023;
  --box-dark:#2b2d30;
  --white:#ffffff;
  --frost:#cee9f5;
  --silver:#d7d7d7;
}
*{margin:0;padding:0;box-sizing:border-box}
html,body{width:1200px;height:853px;overflow:hidden;background:var(--white)}
body{position:relative;font-family:"Source Sans 3",Arial,sans-serif;color:var(--white)}
.spread{position:absolute;left:22px;top:22px;width:1156px;height:796px;
  background:radial-gradient(ellipse at 50% 40%,#2a2e32 0%,var(--panel-dark) 55%,var(--ink) 100%);overflow:hidden}
.footer-band{position:absolute;left:22px;top:818px;width:1156px;height:12px;background:var(--bright-blue)}
.abs{position:absolute}
.body-copy{font-size:15.4px;line-height:18.7px;text-align:center;color:var(--white)}
.heading{font-weight:700;color:var(--bright-blue);text-align:center;font-size:25px;line-height:30px}

/* left panel */
.athletes-photo{left:0;top:0;width:376px;height:270px;
  background:linear-gradient(180deg,#7fb6d8 0%,#4a86b2 35%,#1f5f8e 60%,#17344a 85%,rgba(29,32,35,0) 100%)}
.title{left:0;width:286px;top:228px;font-family:"Roboto Condensed",Arial,sans-serif;font-weight:900;
  font-size:32px;line-height:30px;text-align:right;color:var(--white);letter-spacing:-.3px}
.title .cryo{color:var(--bright-blue)}
.about-h{left:18px;top:333px;width:340px}
.about-copy{left:14px;top:372px;width:348px}
.how-box{left:13px;top:561px;width:348px;height:224px;background:var(--box-dark)}
.how-box h2{margin-top:8px}
.how-copy{margin:8px 12px 0;font-size:14.8px;line-height:18px}
.faq{margin:8px 16px 0;font-size:12.5px;line-height:15px;color:var(--silver)}
.faq dt{font-weight:700;color:var(--bright-blue);display:inline}
.faq dd{display:inline;margin-left:4px}

/* middle panel */
.applications-h{left:376px;top:28px;width:402px}
.applications-copy{left:398px;top:68px;width:358px}
.anatomy-art{left:436px;top:248px;width:290px;height:300px;
  background:radial-gradient(ellipse at 50% 45%,rgba(255,255,255,.35) 0%,rgba(120,190,230,.55) 25%,rgba(30,110,170,.55) 50%,rgba(29,32,35,0) 75%)}
.price-bar{left:393px;top:563px;width:370px;height:40px;background:var(--bright-blue);
  color:var(--ink);font-weight:700;font-size:24px;text-align:center;line-height:40px}
.price-list{left:410px;top:614px;width:336px;list-style:none}
.price-list li{display:flex;align-items:baseline;font-size:15px;line-height:23px}
.price-list .service{white-space:nowrap}
.price-list .leader{flex:1;border-bottom:1px dotted rgba(255,255,255,.4);margin:0 6px}
.price-list .price{font-weight:700;color:var(--bright-blue)}
.hours{left:398px;top:724px;width:358px;font-size:14px;line-height:18px;text-align:center;color:var(--silver)}
.hours strong{color:var(--white);font-weight:700;display:block;font-size:15px}

/* right panel */
.spa-photo{left:778px;top:0;width:378px;height:300px;
  background:linear-gradient(160deg,#b9d9ec 0%,#8fc1dc 40%,#6d9fbd 75%,#4d7fa0 100%)}
.spa-curve{left:778px;top:240px}
.badge{left:960px;top:260px;width:186px;height:186px;border-radius:50%;
  background:var(--ink);border:9px solid var(--bright-blue)}
.badge-text{left:960px;top:310px;width:186px;text-align:center;font-family:"Roboto Condensed",Arial,sans-serif;font-weight:700;color:var(--bright-blue);line-height:50px}
.badge-text .just{font-size:34px}
.badge-text .in{font-size:26px;margin-left:4px}
.badge-text .num{font-size:48px;margin-left:1px}
.badge-text .min{position:absolute;left:104px;top:42px;font-family:"Source Sans 3",Arial,sans-serif;font-weight:600;font-size:17px;line-height:20px;color:var(--white)}
.sectors{left:806px;top:406px;font-weight:700;font-size:25.5px;line-height:37px;letter-spacing:.3px;color:var(--white)}
.brand-name{left:806px;top:524px;display:flex;align-items:center;gap:8px;font-weight:700;font-size:15px;letter-spacing:1.5px;color:var(--bright-blue)}
.brand-dot{width:10px;height:10px;border-radius:50%;background:var(--bright-blue)}
.benefits-box{left:790px;top:561px;width:351px;height:224px;background:var(--box-dark)}
.benefits-box h2{margin-top:9px}
.benefit-cols{display:flex;gap:12px;margin:8px 0 0 14px}
.benefit-cols ul{list-style:none;width:160px}
.benefit-cols li{display:flex;align-items:flex-start;font-size:13.3px;line-height:15px;margin-bottom:3px;color:var(--white)}
.tick{flex:0 0 15px;width:15px;height:15px;margin-right:8px}
</style>
</head>
<body>
<main class="spread">
  <!-- left panel -->
  <div class="abs athletes-photo" role="img" aria-label="Photo of athletes: a cyclist, a runner and a swimmer in open water under a blue sky"></div>
  <h1 class="abs title">WHOLE<br>BODY<br><span class="cryo">CRYO</span>THERAPY</h1>
  <h2 class="abs heading about-h">About</h2>
  <p class="abs body-copy about-copy">Whole Body Cryotherapy (WBC) is a hypothermic application designed to reduce muscoloskeletal pain and inflammation. WBC stimulates the nervous system through skin receptors, causing dramatic peripheral vasoconstriction. This induces adaptive changes correlating with effects of analgesia, reduction of inflammation, and increases in serum markers of tissue repair.</p>
  <section class="abs how-box">
    <h2 class="heading">How it works?</h2>
    <p class="body-copy how-copy">Because of the intense cold, your body will react by sending blood to your core, and in turn will release anti-inflammatory molecules and endorphins. Research shows whole body Cryotherapy can impact your circulatory, energy and nervous systems.</p>
    <dl class="faq">
      <div><dt>FAQ: How long?</dt><dd>Just 3 minutes per session.</dd></div>
      <div><dt>What to wear?</dt><dd>Socks, gloves and shorts, provided.</dd></div>
    </dl>
  </section>

  <!-- middle panel -->
  <h2 class="abs heading applications-h">Applications</h2>
  <p class="abs body-copy applications-copy">Whole Body Cryotherapy (WBC) is a hypothermic application designed to reduce muscoloskeletal pain and inflammation. WBC stimulates the nervous system through skin receptors, causing dramatic peripheral vasoconstriction. This induces adaptive changes correlating with effects of analgesia, reduction of inflammation, and increases in serum markers of tissue repair.</p>
  <div class="abs anatomy-art" role="img" aria-label="Illustration of a translucent blue human torso with the spine highlighted in red"></div>
  <h2 class="abs price-bar">Price Plan</h2>
  <ul class="abs price-list">
    <li><span class="service">Single Session</span><span class="leader"></span><span class="price">$45</span></li>
    <li><span class="service">5-Session Pack</span><span class="leader"></span><span class="price">$200</span></li>
    <li><span class="service">10-Session Pack</span><span class="leader"></span><span class="price">$380</span></li>
    <li><span class="service">Monthly Unlimited</span><span class="leader"></span><span class="price">$299</span></li>
  </ul>
  <p class="abs hours"><strong>Hours</strong>Mon–Fri 7am–8pm · Sat 8am–4pm<br>Sunday by appointment</p>

  <!-- right panel -->
  <div class="abs spa-photo" role="img" aria-label="Photo of a smiling woman standing in a cryotherapy chamber with cold vapour"></div>
  <svg class="abs spa-curve" width="378" height="80" viewBox="0 0 378 80" aria-hidden="true">
    <path d="M0 70 C90 30 200 25 378 40 L378 80 L0 80 Z" fill="#1d2023"/>
    <path d="M0 58 C90 22 200 16 378 30 L378 40 C200 25 90 30 0 70 Z" fill="#1fb4e6"/>
  </svg>
  <div class="abs badge"></div>
  <div class="abs badge-text"><span class="just">Just</span><span class="in">in</span><span class="num">3</span><span class="min">MIN</span></div>
  <p class="abs sectors">BEAUTY &amp; SPA<br>SPORTS &amp; FITNESS<br>HEALTH &amp; WELLNESS</p>
  <p class="abs brand-name"><span class="brand-dot"></span>TIDEWELL CRYOTHERAPY</p>
  <section class="abs benefits-box">
    <h2 class="heading">Benefits</h2>
    <div class="benefit-cols">
      <ul>
        <li><svg class="tick" viewBox="0 0 16 16"><circle cx="8" cy="8" r="8" fill="#1fb4e6"/><path d="M4.3 8.3l2.4 2.4 5-5" stroke="#fff" stroke-width="2" fill="none"/></svg>Pain Management</li>
        <li><svg class="tick" viewBox="0 0 16 16"><circle cx="8" cy="8" r="8" fill="#1fb4e6"/><path d="M4.3 8.3l2.4 2.4 5-5" stroke="#fff" stroke-width="2" fill="none"/></svg>Rapid Muscle Recovery</li>
        <li><svg class="tick" viewBox="0 0 16 16"><circle cx="8" cy="8" r="8" fill="#1fb4e6"/><path d="M4.3 8.3l2.4 2.4 5-5" stroke="#fff" stroke-width="2" fill="none"/></svg>Injury Therapy</li>
        <li><svg class="tick" viewBox="0 0 16 16"><circle cx="8" cy="8" r="8" fill="#1fb4e6"/><path d="M4.3 8.3l2.4 2.4 5-5" stroke="#fff" stroke-width="2" fill="none"/></svg>Performance<br>Enhancement</li>
        <li><svg class="tick" viewBox="0 0 16 16"><circle cx="8" cy="8" r="8" fill="#1fb4e6"/><path d="M4.3 8.3l2.4 2.4 5-5" stroke="#fff" stroke-width="2" fill="none"/></svg>Increased Energy Levels</li>
        <li><svg class="tick" viewBox="0 0 16 16"><circle cx="8" cy="8" r="8" fill="#1fb4e6"/><path d="M4.3 8.3l2.4 2.4 5-5" stroke="#fff" stroke-width="2" fill="none"/></svg>Increased Libido</li>
        <li><svg class="tick" viewBox="0 0 16 16"><circle cx="8" cy="8" r="8" fill="#1fb4e6"/><path d="M4.3 8.3l2.4 2.4 5-5" stroke="#fff" stroke-width="2" fill="none"/></svg>Sleep Better</li>
        <li><svg class="tick" viewBox="0 0 16 16"><circle cx="8" cy="8" r="8" fill="#1fb4e6"/><path d="M4.3 8.3l2.4 2.4 5-5" stroke="#fff" stroke-width="2" fill="none"/></svg>Better Mood</li>
      </ul>
      <ul>
        <li><svg class="tick" viewBox="0 0 16 16"><circle cx="8" cy="8" r="8" fill="#1fb4e6"/><path d="M4.3 8.3l2.4 2.4 5-5" stroke="#fff" stroke-width="2" fill="none"/></svg>Pain Management</li>
        <li><svg class="tick" viewBox="0 0 16 16"><circle cx="8" cy="8" r="8" fill="#1fb4e6"/><path d="M4.3 8.3l2.4 2.4 5-5" stroke="#fff" stroke-width="2" fill="none"/></svg>Rapid Muscle Recovery</li>
        <li><svg class="tick" viewBox="0 0 16 16"><circle cx="8" cy="8" r="8" fill="#1fb4e6"/><path d="M4.3 8.3l2.4 2.4 5-5" stroke="#fff" stroke-width="2" fill="none"/></svg>Injury Therapy</li>
        <li><svg class="tick" viewBox="0 0 16 16"><circle cx="8" cy="8" r="8" fill="#1fb4e6"/><path d="M4.3 8.3l2.4 2.4 5-5" stroke="#fff" stroke-width="2" fill="none"/></svg>Performance<br>Enhancement</li>
        <li><svg class="tick" viewBox="0 0 16 16"><circle cx="8" cy="8" r="8" fill="#1fb4e6"/><path d="M4.3 8.3l2.4 2.4 5-5" stroke="#fff" stroke-width="2" fill="none"/></svg>Increased Energy Levels</li>
        <li><svg class="tick" viewBox="0 0 16 16"><circle cx="8" cy="8" r="8" fill="#1fb4e6"/><path d="M4.3 8.3l2.4 2.4 5-5" stroke="#fff" stroke-width="2" fill="none"/></svg>Increased Libido</li>
        <li><svg class="tick" viewBox="0 0 16 16"><circle cx="8" cy="8" r="8" fill="#1fb4e6"/><path d="M4.3 8.3l2.4 2.4 5-5" stroke="#fff" stroke-width="2" fill="none"/></svg>Sleep Better</li>
        <li><svg class="tick" viewBox="0 0 16 16"><circle cx="8" cy="8" r="8" fill="#1fb4e6"/><path d="M4.3 8.3l2.4 2.4 5-5" stroke="#fff" stroke-width="2" fill="none"/></svg>Better Mood</li>
      </ul>
    </div>
  </section>
</main>
<div class="footer-band"></div>
</body>
</html>
```